Business Card Design

We need a business card designed for our new company. Prefer a black card with white logo & writing.

Contact Information for Business Card

Dale Pickett, address: 7-4417 Larchmere Avenue, Abbotsford, BC, V3K 2R9, Office Phone: 604-555-0172, Cell: 604-555-0138, Email: dale@kelsoncoatworks.ca

Colors

Designer to choose only greyscale colors for use in the design.

```html
<!DOCTYPE html>
<html lang="en">
<head>
<meta charset="utf-8">
<title>Kelson Coatworks – Business Card</title>
<link rel="stylesheet" href="https://fonts.googleapis.com/css2?family=Poppins:wght@400;700&display=swap">
<style>
  :root {
    --backdrop: #d4d5d7;
    --card: #0b0b0b;
    --ink: #ffffff;
    --ink-soft: #e6e6e6;
  }
  * { box-sizing: border-box; margin: 0; padding: 0; }
  html, body {
    width: 900px; height: 1200px; overflow: hidden;
    background: var(--backdrop);
    font-family: "Poppins", sans-serif;
    color: var(--ink);
  }
  .card {
    position: absolute;
    width: 632px; height: 360px;
    background: var(--card);
  }
  .card--front { left: 134px; top: 212px; }
  .card--back  { left: 135px; top: 629px; }

  .brand {
    position: absolute;
    display: flex; align-items: center; gap: 12px;
    font-weight: 700; color: var(--ink);
    white-space: nowrap;
  }
  .brand__mark { background: var(--ink); flex: none; }
  .card--front .brand {
    left: 50%; top: 50%; transform: translate(-50%, -50%);
    font-size: 36px;
  }
  .card--front .brand__mark { width: 22px; height: 22px; }
  .card--back .brand {
    left: 172px; top: 180px; transform: translate(-50%, -50%);
    font-size: 23px; gap: 8px;
  }
  .card--back .brand__mark { width: 14px; height: 14px; }

  .divider {
    position: absolute; left: 340px; top: 88px;
    width: 2px; height: 182px; background: var(--ink);
  }
  .contact {
    position: absolute; left: 374px; top: 84px;
  }
  .contact__name {
    font-weight: 700; font-size: 23px; line-height: 1.2;
    letter-spacing: 0.3px; text-transform: uppercase;
  }
  .contact__role {
    font-size: 14px; color: var(--ink-soft); margin-top: 2px;
  }
  .contact__address {
    font-size: 14px; line-height: 21px; color: var(--ink-soft);
    margin-top: 10px; font-style: normal;
  }
  .contact__list { list-style: none; margin-top: 12px; }
  .contact__item {
    display: flex; align-items: center; gap: 8px;
    font-size: 14.5px; line-height: 22.5px; color: var(--ink-soft);
  }
  .contact__item--phone { letter-spacing: 2px; }
  .contact__item svg { width: 13px; height: 13px; flex: none; fill: var(--ink); }
</style>
</head>
<body>

<section class="card card--front" aria-label="Card front">
  <div class="brand"><span class="brand__mark"></span>Kelson Coatworks</div>
</section>

<section class="card card--back" aria-label="Card back">
  <div class="brand"><span class="brand__mark"></span>Kelson Coatworks</div>
  <div class="divider"></div>
  <div class="contact">
    <h1 class="contact__name">Dale Pickett</h1>
    <p class="contact__role">Manager</p>
    <address class="contact__address">7-4417 Larchmere Avenue,<br>Abbotsford, BC, V3K 2R9</address>
    <ul class="contact__list">
      <li class="contact__item contact__item--phone">
        <svg viewBox="0 0 24 24"><path d="M6.6 10.8a15.1 15.1 0 0 0 6.6 6.6l2.2-2.2c.3-.3.7-.4 1-.2 1.1.4 2.3.6 3.6.6.6 0 1 .4 1 1V20c0 .6-.4 1-1 1A17 17 0 0 1 3 4c0-.6.4-1 1-1h3.5c.6 0 1 .4 1 1 0 1.3.2 2.5.6 3.6.1.3 0 .7-.2 1z"/></svg>
        604-555-0172
      </li>
      <li class="contact__item contact__item--phone">
        <svg viewBox="0 0 24 24"><path d="M7 1h10a2 2 0 0 1 2 2v18a2 2 0 0 1-2 2H7a2 2 0 0 1-2-2V3a2 2 0 0 1 2-2zm0 3v14h10V4zm5 15.5a1.2 1.2 0 1 0 0 2.4 1.2 1.2 0 0 0 0-2.4z"/></svg>
        604-555-0138
      </li>
      <li class="contact__item">
        <svg viewBox="0 0 24 24"><path d="M2 5h20v14H2zm2 2v.4l8 5 8-5V7z"/></svg>
        dale@kelsoncoatworks.ca
      </li>
      <li class="contact__item">
        <svg viewBox="0 0 24 24"><path d="M12 2a10 10 0 1 0 0 20 10 10 0 0 0 0-20zm6.9 6h-2.9a15 15 0 0 0-1.4-3.6A8 8 0 0 1 18.9 8zM12 4c.8 1.2 1.5 2.5 1.9 4h-3.8c.4-1.5 1.1-2.8 1.9-4zM4.3 14a8 8 0 0 1 0-4h3.4a16 16 0 0 0 0 4zm.8 2h2.9c.3 1.3.8 2.5 1.4 3.6A8 8 0 0 1 5.1 16zM8 8H5.1a8 8 0 0 1 4.3-3.6C8.8 5.5 8.4 6.7 8 8zm4 12c-.8-1.2-1.5-2.5-1.9-4h3.8c-.4 1.5-1.1 2.8-1.9 4zm2.3-6H9.7a14 14 0 0 1 0-4h4.6a14 14 0 0 1 0 4zm.3 5.6c.6-1.1 1.1-2.3 1.4-3.6h2.9a8 8 0 0 1-4.3 3.6zm1.7-5.6a16 16 0 0 0 0-4h3.4a8 8 0 0 1 0 4z"/></svg>
        www.kelsoncoatworks.ca
      </li>
    </ul>
  </div>
</section>

</body>
</html>
```